Tidal Fern Business Cards

We need something new, fun and exciting for business cards. Our current ones are just plain and we need a design that pops. We want name, position held, phone, email on the front, and a 20% discount on the back. I have also uploaded our old business cards creative to see what we are not wanting, and how boring they were and we want something jazzed up from this, cool design and catches people attention.

```html
<!DOCTYPE html>
<html lang="en">
<head>
<meta charset="UTF-8">
<title>Tidal Fern Business Cards</title>
<link rel="stylesheet" href="https://fonts.googleapis.com/css2?family=Poppins:wght@300;400;500;700;800&display=swap">
<style>
  :root {
    --navy: #1f3a6b;
    --coral: #ef6f6c;
    --plum: #7e4f78;
    --deep: #2a4174;
    --white: #ffffff;
    --stage: #e9e9ec;
    --divider: #33507f;
  }
  * { box-sizing: border-box; margin: 0; padding: 0; }
  html, body {
    width: 1200px;
    height: 900px;
    overflow: hidden;
    background: var(--stage);
    font-family: "Poppins", sans-serif;
  }
  .sheet {
    width: 1200px;
    height: 900px;
    display: flex;
    flex-direction: column;
    align-items: center;
    justify-content: center;
    gap: 56px;
  }
  .card {
    width: 640px;
    height: 366px;
    position: relative;
    overflow: hidden;
    box-shadow: 0 10px 30px rgba(20, 20, 40, 0.18);
  }

  /* Front */
  .card-front {
    background: var(--white);
    display: flex;
    align-items: center;
  }
  .brand {
    width: 330px;
    display: flex;
    align-items: center;
    justify-content: center;
    gap: 12px;
  }
  .brand-dot {
    width: 18px;
    height: 18px;
    border-radius: 50%;
    background: var(--coral);
  }
  .brand-name {
    font-size: 40px;
    font-weight: 500;
    color: var(--navy);
    letter-spacing: -0.5px;
  }
  .divider {
    width: 1px;
    height: 120px;
    background: var(--divider);
  }
  .contact {
    padding-left: 34px;
  }
  .person-name {
    font-size: 28px;
    color: var(--navy);
    line-height: 1.1;
  }
  .person-name .first { font-weight: 800; }
  .person-name .last { font-weight: 400; }
  .person-role {
    font-size: 15px;
    color: var(--coral);
    margin: 4px 0 16px;
  }
  .contact-line {
    display: flex;
    align-items: center;
    gap: 10px;
    font-size: 15px;
    color: var(--navy);
    margin-bottom: 6px;
  }
  .contact-icon {
    width: 18px;
    height: 18px;
    flex: none;
  }

  /* Back */
  .card-back {
    background: linear-gradient(100deg, var(--coral) 0%, var(--plum) 50%, var(--deep) 100%);
    display: flex;
    align-items: center;
    justify-content: center;
  }
  .offer-frame {
    border: 1.5px solid var(--white);
    padding: 18px 40px 20px;
    text-align: center;
    color: var(--white);
  }
  .offer-value {
    font-size: 96px;
    font-weight: 700;
    line-height: 1;
    letter-spacing: -2px;
  }
  .offer-label {
    font-size: 36px;
    font-weight: 300;
    letter-spacing: 3px;
    line-height: 1.1;
  }
</style>
</head>
<body>
  <main class="sheet">
    <section class="card card-front">
      <div class="brand">
        <span class="brand-dot"></span>
        <span class="brand-name">Tidal Fern</span>
      </div>
      <div class="divider"></div>
      <div class="contact">
        <p class="person-name"><span class="first">Marcus</span> <span class="last">Hale</span></p>
        <p class="person-role">Managing Director</p>
        <p class="contact-line">
          <svg class="contact-icon" viewBox="0 0 20 20" aria-hidden="true">
            <circle cx="10" cy="10" r="10" fill="#ef6f6c"/>
            <path d="M7 5.5c.6-.3 1.1 0 1.4.6l.6 1.3c.2.5 0 .9-.4 1.2l-.5.4c.4 1 1.2 1.8 2.2 2.2l.4-.5c.3-.4.8-.6 1.2-.4l1.3.6c.6.3.9.8.6 1.4-.5 1.1-1.6 1.5-2.7 1.1-2.2-.8-4-2.6-4.8-4.8-.4-1.1 0-2.3 1.1-2.7z" fill="#ffffff"/>
          </svg>
          014 386 2751
        </p>
        <p class="contact-line">
          <svg class="contact-icon" viewBox="0 0 20 20" aria-hidden="true">
            <circle cx="10" cy="10" r="10" fill="#ef6f6c"/>
            <rect x="5" y="6.5" width="10" height="7" rx="1" fill="none" stroke="#ffffff" stroke-width="1.3"/>
            <path d="M5.4 7l4.6 3.6L14.6 7" fill="none" stroke="#ffffff" stroke-width="1.3"/>
          </svg>
          info@tidalfern.com
        </p>
      </div>
    </section>

    <section class="card card-back">
      <div class="offer-frame">
        <p class="offer-value">20%</p>
        <p class="offer-label">DISCOUNT</p>
      </div>
    </section>
  </main>
</body>
</html>
```